Business Card Design

Attached is the logo of the store.

Information needed on the business card:

www.vault82vino.com
info@vault82vino.com
412 7th Ave NY, NY 10036
Tel:(646) 555-0147

Store Hours
Mon-Sat Noon-10pm
Sun Noon-8pm

Free Deliveries

Industry/Entity Type

Business

Contact Information for Business Card

Bramble 82 Wine & Spirits

```html
<!DOCTYPE html>
<html lang="en">
<head>
<meta charset="utf-8">
<title>Bramble 82 Wine &amp; Spirits – Business Card</title>
<link href="https://fonts.googleapis.com/css2?family=Didact+Gothic&display=swap" rel="stylesheet">
<style>
  :root {
    --backdrop: #8c8c8e;
    --card-black: #1a1315;
    --card-brown: #2d1916;
    --card-brown-deep: #1f100e;
    --wine-red: #a8222f;
    --wine-red-soft: rgba(200, 38, 56, 0.55);
    --text-light: #f3eeee;
    --text-soft: #d9cfd0;
  }
  * { margin: 0; padding: 0; box-sizing: border-box; }
  html, body { width: 1200px; height: 900px; overflow: hidden; }
  body {
    background: var(--backdrop);
    font-family: "Didact Gothic", "Century Gothic", sans-serif;
    position: relative;
  }
  .card {
    position: absolute;
    left: 320px;
    width: 560px;
    height: 320px;
    overflow: hidden;
    box-shadow: 0 10px 28px rgba(0,0,0,0.35);
  }
  .card--front { top: 90px; background: var(--card-black); }
  .card--back {
    top: 480px;
    background: radial-gradient(ellipse at 45% 40%, var(--card-brown) 0%, var(--card-brown-deep) 100%);
  }
  .card__bands { position: absolute; inset: 0; }

  .ribbon-area {
    position: absolute;
    left: 0;
    top: 0;
    width: 120px;
    height: 320px;
    background: linear-gradient(90deg, var(--wine-red-soft) 0%, rgba(168, 34, 47, 0) 100%);
  }

  .brand { position: absolute; color: var(--text-light); font-weight: 400; }
  .brand__name { display: block; line-height: 1; letter-spacing: 1px; }
  .brand__tagline { display: block; color: var(--text-soft); letter-spacing: 0.5px; }

  .card--front .brand { left: 215px; top: 42px; }
  .card--front .brand__name { font-size: 46px; }
  .card--front .brand__tagline { font-size: 18px; margin-top: 8px; padding-left: 4px; }

  .card--back .brand { left: 0; right: 0; top: 98px; text-align: center; }
  .card--back .brand__name { font-size: 62px; }
  .card--back .brand__tagline { font-size: 22px; margin-top: 12px; }

  .contact {
    position: absolute;
    left: 42px;
    top: 196px;
    list-style: none;
    color: var(--text-light);
    font-size: 13px;
    line-height: 16px;
  }
  .hours {
    position: absolute;
    left: 340px;
    top: 196px;
    width: 180px;
    text-align: center;
    color: var(--text-light);
    font-size: 13px;
    line-height: 16px;
  }
  .hours__perk { font-size: 18px; margin-top: 6px; line-height: 20px; }
</style>
</head>
<body>

<section class="card card--front" aria-label="Business card front">
  <svg class="card__bands" width="560" height="320" viewBox="0 0 560 320" aria-hidden="true">
    <rect x="0" y="168" width="560" height="5" fill="var(--wine-red)"/>
    <rect x="0" y="180" width="560" height="108" fill="var(--wine-red)"/>
    <rect x="0" y="300" width="560" height="3" fill="var(--wine-red)"/>
  </svg>

  <div class="ribbon-area" role="img" aria-label="Red flowing ribbon ornament along the left edge"></div>

  <div class="brand">
    <span class="brand__name">Bramble 82</span>
    <span class="brand__tagline">wine &amp; spirits</span>
  </div>

  <ul class="contact">
    <li>www.vault82vino.com</li>
    <li>info@vault82vino.com</li>
    <li>412 7th Ave NY, NY 10036</li>
    <li>Tel:(646) 555-0147</li>
  </ul>

  <div class="hours">
    <p>Store Hours</p>
    <p>Mon-Sat Noon-10pm</p>
    <p>Sun Noon-8pm</p>
    <p class="hours__perk">Free Deliveries</p>
  </div>
</section>

<section class="card card--back" aria-label="Business card back">
  <div class="brand">
    <span class="brand__name">Bramble 82</span>
    <span class="brand__tagline">wine &amp; spirits</span>
  </div>
</section>

</body>
</html>
```